Verdant Pathworks Business Card

want the back of card to be blue- with the logo in the center
front of card- info plus logo (info being mailing address, email address, and website address )
4 different names with titles to have on cards
1) Dominic Ashvale - Owner
2) Bethany Korvuth- Customer Relationship Specialist
3) Luca Brennwick- Vice President of Sales
4) Neil Umbright- Chief Technology Officer

Target Market(s)

tech company in the government/probation office industry

Industry/Entity Type

Government Office

Contact Information for Business Card

1) Dominic Ashvale - Owner

Colors
0355a3
ffffff

Requirements
Must have
• back side should be blue, with the logo placed in the center
• front side needs to include both the logo, as well as company info (info should include website address, email address, and mailing address)

```html
<!DOCTYPE html>
<html lang="en">
<head>
<meta charset="UTF-8">
<title>Verdant Pathworks Business Card</title>
<link href="https://fonts.googleapis.com/css2?family=EB+Garamond:wght@700&family=Roboto:wght@400&display=swap" rel="stylesheet">
<style>
  :root {
    --navy: #172b52;
    --white: #ffffff;
    --grey: #7b7b7b;
    --backdrop: #e8e5e1;
  }
  * { margin: 0; padding: 0; box-sizing: border-box; }
  html, body { width: 1125px; height: 1200px; overflow: hidden; }
  body {
    background: var(--backdrop);
    font-family: "Roboto", Arial, sans-serif;
    position: relative;
  }
  .card {
    position: absolute;
    left: 171px;
    width: 827px;
    height: 472px;
    overflow: hidden;
  }
  .card-front { top: 106px; background: var(--white); }
  .card-back { top: 640px; background: var(--navy); }

  .holder { position: absolute; left: 51px; top: 60px; }
  .holder-name {
    font-family: "EB Garamond", Georgia, serif;
    font-weight: 700;
    font-size: 34px;
    color: var(--navy);
    line-height: 1;
  }
  .holder-title {
    font-size: 20px;
    color: var(--grey);
    margin-top: 6px;
  }

  .brand {
    position: absolute;
    display: flex;
    align-items: center;
    gap: 14px;
    font-family: "EB Garamond", Georgia, serif;
    font-weight: 700;
  }
  .brand-front { right: 76px; top: 62px; font-size: 38px; color: var(--navy); }
  .brand-back {
    left: 0; right: 0; top: 0; bottom: 0;
    justify-content: center;
    font-size: 46px;
    color: var(--white);
  }
  .brand-dot { width: 22px; height: 22px; border-radius: 50%; background: currentColor; }

  .contact-band {
    position: absolute;
    left: 0; right: 0; bottom: 0;
    height: 186px;
    background: var(--navy);
    color: var(--white);
    padding: 22px 0 0 51px;
    font-size: 19px;
  }
  .address { line-height: 27px; }
  .contact-list { list-style: none; margin-top: 8px; }
  .contact-list li { display: flex; align-items: center; gap: 12px; height: 26px; }
  .contact-list svg { width: 18px; height: 18px; flex: none; }
</style>
</head>
<body>
  <section class="card card-front">
    <div class="holder">
      <div class="holder-name">Luca Brennwick</div>
      <div class="holder-title">Vice President of Sales</div>
    </div>
    <div class="brand brand-front"><span class="brand-dot"></span>Verdant Pathworks</div>
    <div class="contact-band">
      <div class="address">2240 Harlow Crossing, Suite B<br>Marlton, GA 30399</div>
      <ul class="contact-list">
        <li>
          <svg viewBox="0 0 18 18" aria-hidden="true"><rect x="4" y="1" width="10" height="16" rx="2" fill="none" stroke="#fff" stroke-width="2"/><rect x="7" y="13" width="4" height="1.6" fill="#fff"/></svg>
          404-555-0187
        </li>
        <li>
          <svg viewBox="0 0 18 18" aria-hidden="true"><rect x="1" y="4" width="16" height="11" fill="#fff"/><path d="M1 4 L9 10 L17 4" fill="none" stroke="#172b52" stroke-width="1.5"/></svg>
          lbrennwick@verdantpathworks.com
        </li>
        <li>
          <svg viewBox="0 0 18 18" aria-hidden="true"><circle cx="9" cy="9" r="8" fill="#fff"/><path d="M5 5 q3 1 3 4 q-2 1 -2 4 M11 3 q1 3 4 3 M12 11 q2 0 3 2" fill="none" stroke="#172b52" stroke-width="1.6"/></svg>
          www.verdantpathworks.com
        </li>
      </ul>
    </div>
  </section>

  <section class="card card-back">
    <div class="brand brand-back"><span class="brand-dot"></span>Verdant Pathworks</div>
  </section>
</body>
</html>
```